Cooler Trailer Rental Flyer

I need a flyer designed to showcase a rental product.

We own two refrigerated Chill Haulers. One trailer is 7’ x 12’. The second trailer is 7’ x 16’. Each unit is a double axle trailer with a cargo capacity of 8000 lbs. The refrigeration unit is 110v and is capable of cooling or freezing with just 12 amps. The 12’ unit comes with a securely mounted generator for stand-alone service needs, and we have a portable generator available if needed for the 16’ unit.

The trailer requires a class III or class IV hitch, with a 2 5/16” ball for towing and a 7-pin two vehicle socket for the trailer wiring.

We offer delivery for $1.40 per loaded mile (we only charge for the miles with the trailer attached, so one way for delivery or pickup). This option may make sense for many reasons, including:
- saving the cost of your time
- saving the cost of fuel
- eliminating your liability for the trailer while towing
- preventing you from having to buy any towing equipment

Our farm is located at 4127 Tamsen Mill Avenue, Byron Center, Michigan 49315. The name of the farm/business is Maple Hollow Farm.

The rental rates are as follows:
$169/day (two day minimum rental required)
$599/week
$1500/month

A $100 deposit is required to reserve the trailer. The deposit is fully refundable up to two weeks prior to the event, 50% up to one week, and non-refundable within one week of the event.

The website for the place we bought the trailer is www.frostvanhaul.example. A link to a video from his website is https://frostvanhaul.example/refrigerated-trailer-videos/

I would like the flyer to be colorful and professional, with photos.
Updates

Several notes: 1. I have added the logo for Maple Hollow Farm. 2. Contact information for the brochure should be as follows: Martin or Rebecca Kowalder Maple Hollow Farm 1874 Maple Hollow Lane SW Byron Center, MI 49315 (555) 014-7290 3. Please note that we are not "FrostVanHaul.example". This is the website for the manufacturer of the trailers.

Here are some rental ideas that might be worth including: Emergencies and Power Outages Food Distributors Food Vendors Restaurants Caterers Ice Vendors Pubs and Microbreweries Resorts Festivals Open Markets Sporting Events Parties Weddings Floral Distributors Meat Processors Hunters

e-mail address is maplehollowfarm@mailbox.example

Target Market(s)

Food distributors, caterers, resorts, events (festivals, weddings, fairs, parades, parties, concerts), restaurants, breweries, farmers markets, vending companies, big game hunters

Font styles to use
Serif
Sans Serif

Colors

Designer to choose colors to be used in the design.

Requirements
Nice to have
• Tri-fold flyer

```html
<!DOCTYPE html>
<html lang="en">
<head>
<meta charset="utf-8">
<title>Maple Hollow Farm – Refrigerated Trailer Rental</title>
<link href="https://fonts.googleapis.com/css2?family=Bebas+Neue&family=Roboto:wght@400&display=swap" rel="stylesheet">
<style>
  :root{
    --blue:#3f7bb6;
    --blue-deep:#3a76b2;
    --blue-light:#6a9ccc;
    --teal:#1ba5b6;
    --white:#ffffff;
    --sky-top:#b9d3ea;
    --sky-mid:#dfe7ee;
    --sand:#cfc7b8;
    --trailer:#e9ecef;
  }
  *{margin:0;padding:0;box-sizing:border-box}
  html,body{width:848px;height:1200px;overflow:hidden;background:var(--white)}
  .flyer{position:relative;width:848px;height:1200px;overflow:hidden;background:var(--white);font-family:"Roboto",Arial,sans-serif}
  .shapes{position:absolute;inset:0}
  .display{font-family:"Bebas Neue",Impact,sans-serif;color:var(--white);line-height:.9;position:absolute}
  .farm-name{right:20px;top:100px;text-align:right}
  .farm-name .line-1{font-size:98px;letter-spacing:1px;display:block}
  .farm-name .line-2{font-size:166px;letter-spacing:1px;display:block;margin-top:-4px}
  .farm-name .line-3{font-size:98px;letter-spacing:1px;display:block;margin-top:-6px}
  .address{right:20px;top:452px;text-align:right;font-size:27px;line-height:1.0}
  .price{left:54px;top:470px;width:243px;text-align:center}
  .price .amount{font-size:86px;display:block}
  .price .unit{font-size:25px;display:block;margin-top:4px}
  .rates-title{left:58px;top:690px;font-size:58px}
  .rates-title .underline{position:absolute;left:0;top:60px;width:112px;height:5px;background:var(--white)}
  .rates-list{left:58px;top:783px;font-size:30px;line-height:43px;list-style:none}
  .unit-photo{position:absolute;width:128px;height:128px;border-radius:50%;border:4px solid var(--white);overflow:hidden}
  .unit-photo.small{left:50px;top:926px}
  .unit-photo.large{left:197px;top:926px}
  .unit-label{font-size:29px;top:1068px}
  .unit-label.small{left:70px}
  .unit-label.large{left:220px}
  .capacity{left:118px;top:1105px;font-size:17px}
  .details{position:absolute;left:388px;top:790px;color:var(--blue-deep);font-size:27px;line-height:31.5px;list-style:none}
</style>
</head>
<body>
<main class="flyer">
  <svg class="shapes" width="848" height="1200" viewBox="0 0 848 1200" aria-hidden="false">
    <defs>
      <linearGradient id="photoTone" x1="0" y1="0" x2="0" y2="1">
        <stop offset="0" stop-color="var(--sky-top)"/>
        <stop offset="0.25" stop-color="var(--sky-mid)"/>
        <stop offset="0.45" stop-color="var(--trailer)"/>
        <stop offset="0.7" stop-color="var(--sand)"/>
        <stop offset="1" stop-color="#bdb4a4"/>
      </linearGradient>
    </defs>
    <rect class="hero-photo" x="0" y="0" width="848" height="780" fill="url(#photoTone)" role="img" aria-label="Photo of white refrigerated trailers parked on a sandy lot"/>
    <polygon class="title-panel" points="378,0 848,0 848,470 700,560 378,560" fill="var(--blue)" opacity="0.88"/>
    <polygon class="accent-chevron" points="560,560 848,470 848,690 700,690" fill="var(--blue-light)" opacity="0.85"/>
    <polygon class="content-white" points="368,755 848,600 848,1200 368,1200" fill="var(--white)"/>
    <polygon class="rates-panel" points="0,620 368,545 368,1200 0,1200" fill="var(--blue)"/>
    <polygon class="price-hex" points="175,418 297,488 297,628 175,698 53,628 53,488" fill="var(--teal)"/>
  </svg>

  <h1 class="display farm-name">
    <span class="line-1">MAPLE</span>
    <span class="line-2">HOLLOW</span>
    <span class="line-3">FARM</span>
  </h1>
  <p class="display address">4127 TAMSEN MILL AVENUE<br>BYRON CENTER<br>MICHIGAN 49315</p>

  <p class="display price"><span class="amount">$1.40</span><span class="unit">PER LOADED MILE</span></p>

  <h2 class="display rates-title">RENTAL RATES<span class="underline"></span></h2>
  <ul class="display rates-list">
    <li>$169/DAY (MIN 2 DAYS)</li>
    <li>$599/WEEK</li>
    <li>$1500/MONTH</li>
  </ul>

  <div class="unit-photo small" role="img" aria-label="Photo of the 7 by 12 foot refrigerated trailer">
    <svg width="120" height="120"><rect width="120" height="120" fill="url(#photoTone)"/></svg>
  </div>
  <div class="unit-photo large" role="img" aria-label="Photo of the 7 by 16 foot refrigerated trailer">
    <svg width="120" height="120"><rect width="120" height="120" fill="url(#photoTone)"/></svg>
  </div>
  <p class="display unit-label small">7’ X 12’</p>
  <p class="display unit-label large">7’ X 16’</p>
  <p class="display capacity">CAPACITY OF 8000 LBS</p>

  <ul class="details">
    <li>The trailer requires a class III<br>or class IV hitch, with a 2 5/16”<br>ball for towing and a 7-pin two<br>vehicle socket for the trailer wiring</li>
    <li>Saving the cost of your time</li>
    <li>Saving the cost of fuel</li>
    <li>Eliminating your liability<br>for the trailer while towing</li>
    <li>Preventing you from having<br>to buy any towing equipment</li>
  </ul>
</main>
</body>
</html>
```